Classy, Elegant, Simple Business Card Design

Looking to have a classy, simple, and elegant design. Want a top notch designed business card. I really like the look of the new brivo credit card. I also like the design I attached. I am trying to reach 21-29 year old females for booking us for there wedding or event. We offer Disc Jockey Service, Photo Booth Rentals, and Uplighting .

Target Market(s)

21-28 year old females

Contact Information for Business Card

Has to have logo, website, email, and phone number

Font styles to use
Other font styles liked:
• open to font choice, modern, clean
Designer to choose
33a6d7
0791cd
0555a3
ffffff

Requirements
Must have
• Has to have logo, website, email, and phone number
Nice to have
• I really like the design of the new brivo credit card. I also included my logo and some designs I like
Should not have
• clutter or too much info

```html
<!DOCTYPE html>
<html lang="en">
<head>
<meta charset="utf-8">
<title>Tideline Event Group – Business Card</title>
<link rel="stylesheet" href="https://fonts.googleapis.com/css2?family=Open+Sans:wght@400;700&display=swap">
<style>
  :root {
    --navy: #0555a3;
    --blue: #0791cd;
    --sky: #33a6d7;
    --paper: #ffffff;
    --ink: #666666;
    --green: #8dc63f;
    --pink: #f06b8f;
    --teal: #35bfbf;
  }
  html, body {
    margin: 0;
    padding: 0;
    width: 1200px;
    height: 720px;
    overflow: hidden;
    background: var(--paper);
  }
  .card {
    position: relative;
    width: 1200px;
    height: 720px;
    background: var(--paper);
    font-family: "Open Sans", Arial, sans-serif;
  }
  .holder-name {
    position: absolute;
    left: 104px;
    top: 104px;
    margin: 0;
    font-size: 84px;
    font-weight: 700;
    letter-spacing: -3px;
    line-height: 1;
    color: var(--navy);
  }
  .holder-role {
    position: absolute;
    left: 165px;
    top: 203px;
    margin: 0;
    font-size: 34px;
    font-weight: 400;
    color: var(--blue);
  }
  .brand {
    position: absolute;
    left: 130px;
    top: 400px;
    width: 305px;
    text-align: center;
  }
  .brand-dot {
    display: block;
    margin: 0 auto 18px;
    width: 110px;
    height: 110px;
    border-radius: 50%;
    background: var(--navy);
  }
  .brand-name {
    font-size: 30px;
    font-weight: 700;
    letter-spacing: 1px;
    color: var(--navy);
    white-space: nowrap;
  }
  .contacts {
    position: absolute;
    left: 657px;
    top: 415px;
    margin: 0;
    padding: 0;
    list-style: none;
  }
  .contact {
    display: flex;
    align-items: center;
    height: 52px;
  }
  .contact-icon {
    width: 53px;
    height: 52px;
    display: flex;
    align-items: center;
    justify-content: center;
  }
  .contact-icon--phone { background: var(--green); }
  .contact-icon--mail { background: var(--pink); }
  .contact-icon--web { background: var(--teal); }
  .contact-text {
    margin-left: 29px;
    font-size: 30px;
    color: var(--ink);
    letter-spacing: 0.3px;
  }
  .services {
    position: absolute;
    left: 0;
    right: 0;
    top: 642px;
    margin: 0;
    padding-left: 38px;
    text-align: center;
    font-size: 21px;
    color: var(--sky);
  }
</style>
</head>
<body>
  <main class="card">
    <h1 class="holder-name">ELLIS MARROW</h1>
    <p class="holder-role">General Manager</p>

    <div class="brand">
      <span class="brand-dot"></span>
      <span class="brand-name">TIDELINE EVENT GROUP</span>
    </div>

    <ul class="contacts">
      <li class="contact">
        <span class="contact-icon contact-icon--phone">
          <svg width="22" height="22" viewBox="0 0 24 24" aria-hidden="true">
            <path d="M6.6 10.8a15.2 15.2 0 0 0 6.6 6.6l2.2-2.2a1 1 0 0 1 1-.25 11.4 11.4 0 0 0 3.6.57 1 1 0 0 1 1 1V20a1 1 0 0 1-1 1A17 17 0 0 1 3 4a1 1 0 0 1 1-1h3.5a1 1 0 0 1 1 1c0 1.25.2 2.45.57 3.57a1 1 0 0 1-.25 1z" fill="#fff"/>
          </svg>
        </span>
        <span class="contact-text">+0201555019372</span>
      </li>
      <li class="contact">
        <span class="contact-icon contact-icon--mail">
          <svg width="22" height="16" viewBox="0 0 22 16" aria-hidden="true">
            <rect x="0" y="0" width="22" height="16" fill="#fff"/>
            <path d="M0 0 L11 9 L22 0" fill="none" stroke="#f06b8f" stroke-width="1.6"/>
          </svg>
        </span>
        <span class="contact-text">info@tidelineevents.com</span>
      </li>
      <li class="contact">
        <span class="contact-icon contact-icon--web">
          <svg width="22" height="22" viewBox="0 0 24 24" aria-hidden="true">
            <g fill="none" stroke="#fff" stroke-width="1.6">
              <circle cx="12" cy="12" r="10"/>
              <ellipse cx="12" cy="12" rx="4.5" ry="10"/>
              <line x1="2" y1="12" x2="22" y2="12"/>
              <path d="M4 6.5h16M4 17.5h16"/>
            </g>
          </svg>
        </span>
        <span class="contact-text">www.tidelineevents.com</span>
      </li>
    </ul>

    <p class="services">We offer Disc Jockey Service, Photo Booth Rentals, and Uplighting</p>
  </main>
</body>
</html>
```